Cellular Repair Flyer

My company uses flyers to post on swapsy board and other media to promote our cellular phone repair's. I'm going to attach a bunch of other flyers that I've seen done that were not branded for my company. But... what i'm looking for is another COOL flyer. i'm not just looking for it to say "hey we do repairs". this flyer... I want the designer to think "cool", "hip".... think "Penny Rowe's" type brand. You know... something cool or hip that maybe shows a broken phone and then just something hip that says we fix phones. Something like (yeah my idea's are weak :) ) but something like... a phone showing a crack in it.... then a guy showing his ass crack. and then a picture that says.... Fix Your Crack... its not cool. so i'm sure you get the drift. something fun... not too edgy though as we don't want to offend kids, women, etc. Something funny.... phone in toilet and then a joke. Stuff that actually could happen to phones. Also... to protect someone in this contest that... lets say comes up with a really cool and funny angle an then others maybe use the same joke but different graphics that we liked better.... the person that comes up with the cool joke or theme will absolutely be selected as well. As a matter of fact probably as first place and then the graphics in 2nd. Bottom line... I just wanted to make sure they you know that I would jake sure we are all being fair with our originality so that will definitely be protected. AND again.... if there were a number of really funny ones I would consider buying a bunch of them as I really need a solid 12+

I attached our first flyer that was created and also our logo.

We sell a TON of cellular accessories at this store (literally everything and really good stuff also. very comparable to a gadget barn) so if you wanted to leverage any graphics I attached a pic of one of our retail walls. Below is also a link to a bunch of the brand names that we carry in accessory products.

Reference our web site www.handsetmendcrew.example (I just launched another contest on here today to completely redesign that web site as well)
Reference our address: 4158 S 41st Street, Milwaukee, Wisconsin 53219
and anytime you use that address state "3 Blocks North of 41st & Harbeck Ave"

Hopefully i'll find a good designer with some more good idea's for these "hip" type of flyers as i'd really like to have about 12 of these. different cool sayings and graphics to go along with it. I'd keep buying them as long as you kept coming up with them.

Target Market(s)

Milwaukee, Wisconsin

Industry/Entity Type

Cell Phone

Requirements
Must have
• Must be cool.... funny, hip... something with some personality
• Thanks in advance and please take a look at the full web site project I listed for this same company!
Nice to have
• use any graphics you want. I included some below but really you can use anything you want. This location "3 blocks North of 41st and Harbeck" is kind of a iconic location for this market. So if someone created some cool graphic that helped highlight this property being 2 b locks south of that intersection... it would likely have a lot of value.
Should not have
• nothing too crude that would offend say your mother.... or your kids. So it can be a little edgy... just not so much that it would offend women and children.

```html
<!DOCTYPE html>
<html lang="en">
<head>
<meta charset="utf-8">
<title>Crack Kills – Phone Repair Flyer</title>
<link rel="stylesheet" href="https://fonts.googleapis.com/css2?family=Open+Sans:wdth,wght@87.5,400&family=Mulish:ital,wght@0,800;1,400&display=swap">
<style>
  :root {
    --paper: #ffffff;
    --ink: #111111;
    --navy: #1e3a5c;
    --device-dark: #07080a;
    --device-mid: #1c1e22;
    --bezel: #3a3c40;
    --glass-light: rgba(205, 210, 216, 0.85);
    --glass-soft: rgba(170, 176, 184, 0.45);
    --shadow: rgba(0, 0, 0, 0.35);
  }
  * { margin: 0; padding: 0; box-sizing: border-box; }
  html, body {
    width: 927px;
    height: 1200px;
    overflow: hidden;
    background: var(--paper);
  }
  .flyer {
    position: relative;
    width: 927px;
    height: 1200px;
    background: var(--paper);
    color: var(--ink);
  }
  .headline {
    position: absolute;
    top: 24px;
    left: 0;
    width: 100%;
    text-align: center;
    font-family: "Open Sans", sans-serif;
    font-stretch: 87.5%;
    font-weight: 400;
    font-size: 84px;
    line-height: 1.2;
    text-shadow: 3px 6px 6px var(--shadow);
  }
  .phone-visual {
    position: absolute;
    top: 163px;
    left: 283px;
    width: 343px;
    height: 668px;
    border-radius: 30px;
    border: 4px solid var(--bezel);
    background:
      radial-gradient(ellipse 55% 30% at 92% 6%, var(--glass-light) 0%, transparent 70%),
      conic-gradient(from 195deg at 96% 4%, transparent 0deg, var(--glass-soft) 12deg, var(--glass-light) 28deg, var(--glass-soft) 48deg, transparent 62deg),
      radial-gradient(ellipse 30% 18% at 25% 14%, rgba(120,126,134,0.4) 0%, transparent 70%),
      radial-gradient(ellipse 70% 8% at 40% 90%, rgba(110,116,124,0.35) 0%, transparent 70%),
      linear-gradient(165deg, var(--device-mid) 0%, var(--device-dark) 70%);
  }
  .phone-reflection {
    position: absolute;
    top: 834px;
    left: 292px;
    width: 326px;
    height: 80px;
    background: linear-gradient(to bottom, rgba(40,42,46,0.14), rgba(255,255,255,0));
  }
  .services {
    position: absolute;
    top: 872px;
    left: 0;
    width: 100%;
    text-align: center;
    font-family: "Mulish", sans-serif;
    font-style: italic;
    font-weight: 400;
    font-size: 38px;
    line-height: 1.2;
    text-shadow: 2px 4px 5px var(--shadow);
  }
  .brand {
    position: absolute;
    top: 1004px;
    left: 0;
    width: 100%;
    text-align: center;
    font-family: "Mulish", sans-serif;
    font-weight: 800;
    font-size: 36px;
    line-height: 1.2;
    color: var(--navy);
  }
  .address {
    position: absolute;
    top: 1068px;
    left: 0;
    width: 100%;
    text-align: center;
    font-family: "Mulish", sans-serif;
    font-style: italic;
    font-size: 27px;
    line-height: 1.2;
  }
  .directions {
    position: absolute;
    top: 1104px;
    left: 0;
    width: 100%;
    text-align: center;
    font-family: "Mulish", sans-serif;
    font-style: italic;
    font-size: 26px;
    line-height: 1.2;
  }
</style>
</head>
<body>
  <main class="flyer">
    <h1 class="headline">CRACK KILLS</h1>
    <div class="phone-visual" role="img" aria-label="Photo of a black smartphone with a badly shattered glass screen, a web of white cracks fanning out from the top right corner across the display"></div>
    <div class="phone-reflection"></div>
    <p class="services">Certified Repairs - Replacements - Accessories</p>
    <p class="brand">www.handsetmendcrew.example</p>
    <p class="address">4158 S. 41st Street, Milwaukee, WI 53219</p>
    <p class="directions">3 Blocks North of 41st &amp; Harbeck Ave</p>
  </main>
</body>
</html>
```